Flyer für ein Küchenfachgeschäft
Zielgruppe
Wir sind ein Küchenfachgeschäft und würden hierfür gerne einen Flyer für Hochwertige und Qualitative Küchen einen Flyer erstellen lassen.
Aufgabenstellung
US gefaltet Format, Hochwertig und ansprechend. Wir sind Berater, Planer und Ausführer. 35 Jahre Erfahrung

```html
<!DOCTYPE html>
<html lang="de">
<head>
<meta charset="utf-8">
<title>Flyer Küchenfachgeschäft</title>
<link rel="stylesheet" href="https://fonts.googleapis.com/css2?family=Noto+Sans:wght@400;700&family=Julius+Sans+One&display=swap">
<style>
  :root {
    --flyer-bg: #1a1c1c;
    --text-light: #ffffff;
    --photo-light: #e4e6e7;
    --photo-mid: #b9bcbe;
    --photo-dark: #2a2b2c;
  }
  * { margin: 0; padding: 0; box-sizing: border-box; }
  html, body {
    width: 1200px;
    height: 2400px;
    overflow: hidden;
    background: var(--flyer-bg);
  }
  .flyer {
    position: relative;
    width: 1200px;
    height: 2400px;
    background: var(--flyer-bg);
    color: var(--text-light);
    font-family: "Noto Sans", "Open Sans", sans-serif;
    overflow: hidden;
  }
  .photo-circle {
    position: absolute;
    display: block;
  }
  .photo-circle--appliances { left: -136px; top: 116px; width: 678px; height: 678px; }
  .photo-circle--tap { left: 462px; top: 1522px; width: 692px; height: 692px; }
  .intro-text, .invitation-text {
    position: absolute;
    text-align: right;
    font-size: 39px;
    line-height: 65px;
    font-weight: 400;
  }
  .intro-text { right: 108px; top: 174px; width: 600px; }
  .invitation-text { right: 97px; top: 798px; width: 800px; }
  .promise-heading {
    position: absolute;
    left: 73px;
    top: 1280px;
    width: 620px;
    font-size: 39px;
    line-height: 65px;
    font-weight: 700;
  }
  .address {
    position: absolute;
    left: 82px;
    top: 2218px;
    font-family: "Julius Sans One", sans-serif;
    font-size: 50px;
    line-height: 67px;
    letter-spacing: 1px;
    text-transform: uppercase;
  }
</style>
</head>
<body>
<main class="flyer">
  <svg class="photo-circle photo-circle--appliances" viewBox="0 0 678 678" role="img" aria-label="Foto: Einbaubackofen und Kaffeevollautomat in weißer Küche mit Marmorrückwand">
    <defs>
      <linearGradient id="appliancesTone" x1="0" y1="0" x2="1" y2="0">
        <stop offset="0" stop-color="var(--photo-dark)"/>
        <stop offset="0.5" stop-color="#3a3b3c"/>
        <stop offset="0.62" stop-color="var(--photo-mid)"/>
        <stop offset="1" stop-color="var(--photo-light)"/>
      </linearGradient>
    </defs>
    <circle cx="339" cy="339" r="339" fill="url(#appliancesTone)"/>
  </svg>

  <p class="intro-text">Willkommen bei [Name des Küchengeschäfts] - Ihrer Quelle für hochwertige Küchenlösungen, die Ihre kulinarischen Träume wahr werden lassen.</p>

  <p class="invitation-text">Tauchen Sie ein in eine Welt voller Eleganz, Funktionalität und zeitlosem Design und lassen Sie uns Ihnen helfen, die Küche Ihrer Träume zu gestalten.</p>

  <h2 class="promise-heading">Unser Versprechen an Sie:<br>Exzellenz in jeder<br>Facette</h2>

  <svg class="photo-circle photo-circle--tap" viewBox="0 0 692 692" role="img" aria-label="Foto: schwarze Küchenarmatur über Spüle vor Marmorwand">
    <defs>
      <linearGradient id="tapTone" x1="0" y1="0" x2="0" y2="1">
        <stop offset="0" stop-color="var(--photo-light)"/>
        <stop offset="0.6" stop-color="#d3d5d6"/>
        <stop offset="0.8" stop-color="#8e9092"/>
        <stop offset="1" stop-color="#cfd1d2"/>
      </linearGradient>
    </defs>
    <circle cx="346" cy="346" r="346" fill="url(#tapTone)"/>
  </svg>

  <address class="address" style="font-style: normal;">Adresse:<br>Strassestrasse 234</address>
</main>
</body>
</html>
```